Real Estate Sales Brokerage

Design a modern and fresh looking standard size business card, incorporate our logo's color scheme and modern appearance with head shot photo on front side and incorporate our log on the back side

Target Market(s)

Residential Home sales

Industry/Entity Type

Real Estate Agent

Font styles to use
Sans Serif

Colors

Designer to choose colors to be used in the design.

Requirements
Must have
• fresh, modern, not too busy, incorporate head shot in front of the card, incorporate logo in front and back of the card. Use logo design scheme as appropriate.
Nice to have
• horizontal and vertical options to compare would be nice.

```html
<!DOCTYPE html>
<html lang="en">
<head>
<meta charset="utf-8">
<title>Harbor Keystone Realty – Business Card</title>
<link href="https://fonts.googleapis.com/css2?family=Open+Sans:wght@400;600;700&display=swap" rel="stylesheet">
<style>
  :root {
    --backdrop: #111111;
    --paper: #ffffff;
    --brand-yellow: #f3d34a;
    --brand-olive: #66663a;
    --ink-olive: #55552c;
    --photo-tone-a: #6f8a8c;
    --photo-tone-b: #c9a48c;
  }
  * { box-sizing: border-box; margin: 0; padding: 0; }
  html, body { width: 1200px; height: 1000px; overflow: hidden; }
  body {
    background: var(--backdrop);
    font-family: "Open Sans", Arial, sans-serif;
    display: flex;
    align-items: center;
    justify-content: center;
    gap: 40px;
  }
  .card {
    position: relative;
    width: 540px;
    height: 309px;
    border-radius: 22px;
    overflow: hidden;
  }
  .card-front { background: var(--paper); }
  .card-back {
    background: var(--brand-yellow);
    display: flex;
    align-items: center;
    justify-content: center;
  }
  .front-shapes { position: absolute; inset: 0; }
  .contact-block {
    position: absolute;
    left: 34px;
    top: 30px;
    color: var(--ink-olive);
  }
  .agent-name { font-size: 20px; font-weight: 700; letter-spacing: 0.5px; line-height: 1.1; }
  .agent-title { font-size: 13px; font-weight: 400; margin-bottom: 14px; }
  .contact-line { font-size: 11px; line-height: 1.5; }
  .brand-front {
    position: absolute;
    left: 34px;
    top: 200px;
    display: flex;
    align-items: center;
    gap: 8px;
    color: var(--ink-olive);
  }
  .brand-mark-square {
    width: 26px; height: 26px;
    background: var(--brand-yellow);
  }
  .brand-name-small {
    font-size: 11px; font-weight: 600; line-height: 1.15; text-transform: uppercase;
  }
  .brand-back {
    display: flex;
    align-items: center;
    gap: 20px;
    color: var(--brand-olive);
  }
  .brand-mark-large {
    width: 70px; height: 70px;
    background: var(--brand-olive);
  }
  .brand-name-large {
    font-size: 28px; font-weight: 600; line-height: 1.1; text-transform: uppercase; letter-spacing: 1px;
  }
</style>
</head>
<body>
  <section class="card card-front">
    <svg class="front-shapes" width="540" height="309" viewBox="0 0 540 309">
      <defs>
        <linearGradient id="headshot-tone" x1="0" y1="0" x2="1" y2="1">
          <stop offset="0" stop-color="var(--photo-tone-a)"/>
          <stop offset="1" stop-color="var(--photo-tone-b)"/>
        </linearGradient>
      </defs>
      <rect class="tile-yellow" x="240" y="140" width="135" height="100" fill="var(--brand-yellow)"/>
      <rect class="headshot" role="img" aria-label="Agent headshot photo" x="388" y="118" width="130" height="110" fill="url(#headshot-tone)"/>
      <polygon class="tile-olive" points="240,252 402,238 420,309 240,309" fill="var(--brand-olive)"/>
      <polygon class="tile-yellow-lower" points="414,237 540,226 540,309 434,309" fill="var(--brand-yellow)"/>
    </svg>
    <div class="contact-block">
      <div class="agent-name">LOREM IPSUM</div>
      <div class="agent-title">Director</div>
      <div class="contact-line">123 456 789</div>
      <div class="contact-line">email_add@domain.com</div>
      <div class="contact-line">HarborKeystoneRealty.com</div>
    </div>
    <div class="brand-front">
      <div class="brand-mark-square"></div>
      <div class="brand-name-small">Harbor<br>Keystone<br>Realty</div>
    </div>
  </section>

  <section class="card card-back">
    <div class="brand-back">
      <div class="brand-mark-large"></div>
      <div class="brand-name-large">Harbor<br>Keystone<br>Realty</div>
    </div>
  </section>
</body>
</html>
```